Business Card Design - Corporate

Create a sleek elegant business card layout while suggesting a color scheme. Convey cutting edge technology while maintaining a corporate feel that is easily readable.

Company designs and manufactures consumer electronic products for mass retail that are mainly app driven.

(vector logo and die-line provided)

Target Market(s)

Corporate level, tech industry.

Industry/Entity Type

Business

Contact Information for Business Card

Generic Info:

Name
Title
email
address
phone 1
phone 2
website (quelvane.com) on back

Font styles to use
Sans Serif

Requirements
Must have
• At least 2 colors + white on one side.
Nice to have
• Solid suggestion on color for logo and overall design. Color flood on back of card.
Should not have
• background texture like... marble, stone, patterns or circuit boards

```html
<!DOCTYPE html>
<html lang="en">
<head>
<meta charset="utf-8">
<title>Quelvane Business Card</title>
<link href="https://fonts.googleapis.com/css2?family=Lato:wght@400;700&family=Roboto+Condensed:wght@700&display=swap" rel="stylesheet">
<style>
  :root {
    --stage: #9a9fa2;
    --ink-dark: #2b2b2b;
    --ink-dark-top: #232323;
    --ink-dark-bottom: #3b3b3b;
    --paper: #ffffff;
    --band-grey: #878585;
    --text: #2a2a2a;
    --rule: #333333;
    --card-edge: #3a3a3a;
  }
  html, body {
    margin: 0;
    padding: 0;
    width: 1200px;
    height: 900px;
    overflow: hidden;
    background: var(--stage);
  }
  .canvas {
    position: relative;
    width: 1200px;
    height: 900px;
    font-family: "Lato", sans-serif;
  }
  .card {
    position: absolute;
    border-radius: 0 46px 0 46px;
    overflow: hidden;
    background: var(--paper);
  }
  .card--front { left: 87px; top: 47px; width: 464px; height: 772px; }
  .card--back { left: 659px; top: 50px; width: 461px; height: 769px; box-sizing: border-box; border: 1px solid var(--card-edge); }

  .front-header {
    position: absolute; left: 0; top: 0; width: 100%; height: 337px;
    background: linear-gradient(180deg, var(--ink-dark-top), var(--ink-dark-bottom));
  }
  .front-footer {
    position: absolute; left: 0; top: 712px; width: 100%; height: 60px;
    background: var(--band-grey);
  }
  .saw { position: absolute; left: 0; width: 464px; height: 12px; display: block; }
  .saw--top { top: 336px; }
  .saw--bottom { top: 701px; }

  .wordmark {
    position: absolute; left: 0; width: 100%;
    text-align: center;
    font-family: "Lato", sans-serif;
    font-weight: 400;
    letter-spacing: 0.3em;
    text-indent: 0.3em;
    line-height: 1;
  }
  .wordmark--light { top: 145px; font-size: 46px; color: var(--paper); }
  .wordmark--dark { top: 356px; font-size: 44px; color: var(--text); }

  .holder-name {
    position: absolute; left: 0; top: 358px; width: 100%;
    text-align: center;
    font-family: "Roboto Condensed", sans-serif;
    font-weight: 700;
    font-size: 43px; line-height: 1;
    color: var(--text);
  }
  .holder-role {
    position: absolute; left: 0; top: 414px; width: 100%;
    text-align: center; font-size: 23px; line-height: 1; color: var(--text);
  }
  .rule { position: absolute; height: 0; border-top: 1.5px solid var(--rule); }
  .front-rule { left: 66px; width: 333px; }
  .front-rule--top { top: 453px; }
  .front-rule--bottom { top: 672px; }
  .back-rule { left: 80px; width: 301px; border-top-width: 1px; }
  .back-rule--top { top: 335px; }
  .back-rule--bottom { top: 432px; }

  .contact-icon { position: absolute; left: 113px; width: 38px; height: 38px; }
  .contact-text {
    position: absolute; left: 154px;
    font-size: 22px; line-height: 27px; color: var(--text);
    white-space: nowrap;
  }
  .contact--phone .contact-icon { top: 464px; }
  .contact--phone .contact-text { top: 458px; }
  .contact--web .contact-icon { top: 545px; }
  .contact--web .contact-text { top: 539px; }
  .contact--place .contact-icon { top: 624px; }
  .contact--place .contact-text { top: 619px; }
</style>
</head>
<body>
<div class="canvas">

  <section class="card card--front">
    <div class="front-header"></div>
    <svg class="saw saw--top" viewBox="0 0 464 12" aria-hidden="true">
      <path fill="#3b3b3b" d="M0 0 l10.545 12 l10.545 -12 l10.545 12 l10.545 -12 l10.545 12 l10.545 -12 l10.545 12 l10.545 -12 l10.545 12 l10.545 -12 l10.545 12 l10.545 -12 l10.545 12 l10.545 -12 l10.545 12 l10.545 -12 l10.545 12 l10.545 -12 l10.545 12 l10.545 -12 l10.545 12 l10.545 -12 l10.545 12 l10.545 -12 l10.545 12 l10.545 -12 l10.545 12 l10.545 -12 l10.545 12 l10.545 -12 l10.545 12 l10.545 -12 l10.545 12 l10.545 -12 l10.545 12 l10.545 -12 l10.545 12 l10.545 -12 l10.545 12 l10.545 -12 l10.545 12 l10.545 -12 l10.545 12 l10.545 -12 l10.545 12 l10.545 -12 Z"/>
    </svg>
    <div class="front-footer"></div>
    <svg class="saw saw--bottom" viewBox="0 0 464 12" aria-hidden="true">
      <path fill="#878585" d="M0 12 l10.545 -12 l10.545 12 l10.545 -12 l10.545 12 l10.545 -12 l10.545 12 l10.545 -12 l10.545 12 l10.545 -12 l10.545 12 l10.545 -12 l10.545 12 l10.545 -12 l10.545 12 l10.545 -12 l10.545 12 l10.545 -12 l10.545 12 l10.545 -12 l10.545 12 l10.545 -12 l10.545 12 l10.545 -12 l10.545 12 l10.545 -12 l10.545 12 l10.545 -12 l10.545 12 l10.545 -12 l10.545 12 l10.545 -12 l10.545 12 l10.545 -12 l10.545 12 l10.545 -12 l10.545 12 l10.545 -12 l10.545 12 l10.545 -12 l10.545 12 l10.545 -12 l10.545 12 l10.545 -12 l10.545 12 l10.545 -12 l10.545 12 Z"/>
    </svg>

    <div class="wordmark wordmark--light">QUELVANE</div>

    <div class="holder-name">YOUR NAME</div>
    <div class="holder-role">Your Position</div>
    <div class="rule front-rule front-rule--top"></div>

    <div class="contact contact--phone">
      <svg class="contact-icon" viewBox="0 0 24 24" aria-hidden="true">
        <path fill="#2a2a2a" d="M6.6 10.8c1.4 2.8 3.8 5.1 6.6 6.6l2.2-2.2c.3-.3.7-.4 1-.2 1.1.4 2.3.6 3.6.6.6 0 1 .4 1 1V20c0 .6-.4 1-1 1C10.6 21 3 13.4 3 4c0-.6.4-1 1-1h3.5c.6 0 1 .4 1 1 0 1.3.2 2.5.6 3.6.1.3 0 .7-.2 1z"/>
      </svg>
      <div class="contact-text">000 - 1234 - 56789<br>000 - 8976 - 54321</div>
    </div>

    <div class="contact contact--web">
      <svg class="contact-icon" viewBox="0 0 24 24" aria-hidden="true">
        <g fill="none" stroke="#2a2a2a" stroke-width="1.6">
          <circle cx="12" cy="12" r="9.5"/>
          <ellipse cx="12" cy="12" rx="4.2" ry="9.5"/>
          <line x1="12" y1="2.5" x2="12" y2="21.5"/>
          <line x1="2.5" y1="12" x2="21.5" y2="12"/>
          <path d="M4 7.2h16M4 16.8h16"/>
        </g>
      </svg>
      <div class="contact-text">admin@quelvane.com<br>www.quelvane.com</div>
    </div>

    <div class="contact contact--place">
      <svg class="contact-icon" viewBox="0 0 24 24" aria-hidden="true">
        <circle cx="12" cy="12" r="9.5" fill="none" stroke="#2a2a2a" stroke-width="2"/>
        <path fill="#2a2a2a" d="M16.5 7.5 13.3 13.3 7.5 16.5 10.7 10.7Z"/>
        <circle cx="12" cy="12" r="1.1" fill="#ffffff"/>
      </svg>
      <div class="contact-text">your address details,<br>place 12345</div>
    </div>

    <div class="rule front-rule front-rule--bottom"></div>
  </section>

  <section class="card card--back">
    <div class="rule back-rule back-rule--top"></div>
    <div class="wordmark wordmark--dark">QUELVANE</div>
    <div class="rule back-rule back-rule--bottom"></div>
  </section>

</div>
</body>
</html>
```